Floor Inspections and Consulting

We provide inspections and consulting services on various floor coverings, e.g. carpet, hardwood, etc. We also do expert witness work for attorneys due to floor covering failures. We current have a logo, just need it incorporated into a new design. I have examples of cards I have found on the internet that capture my attention and make a statement. I have included our original business card, which in my opinion is terrible, but it does have our logo on it.

```html
<!DOCTYPE html>
<html lang="en">
<head>
<meta charset="utf-8">
<title>Summit Floor Inspections – Business Card</title>
<link rel="stylesheet" href="https://fonts.googleapis.com/css2?family=Questrial&display=swap">
<style>
  :root {
    --page-bg: #ffffff;
    --orange-top: #f7941d;
    --orange-bottom: #f15a2b;
    --orange-accent: #f26b22;
    --card-black: #1e1e1e;
    --ink-dark: #1b1b1b;
    --white: #ffffff;
  }
  * { margin: 0; padding: 0; box-sizing: border-box; }
  html, body {
    width: 1200px; height: 900px; overflow: hidden;
    background: var(--page-bg);
    font-family: "Questrial", "Century Gothic", sans-serif;
  }
  .canvas {
    width: 1200px; height: 900px;
    display: flex; align-items: center; justify-content: center; gap: 44px;
  }
  .card {
    position: relative;
    width: 520px; height: 300px;
    border-radius: 22px;
    overflow: hidden;
    display: flex; flex-direction: column; align-items: center;
  }
  .card-edges { position: absolute; inset: 0; width: 100%; height: 100%; }
  .card-front { background: linear-gradient(180deg, var(--orange-top), var(--orange-bottom)); }
  .card-back { background: var(--card-black); justify-content: center; }

  .brand { position: relative; display: flex; flex-direction: column; align-items: center; gap: 6px; color: var(--white); }
  .brand-mark { width: 16px; height: 16px; background: var(--white); }
  .brand-name { font-size: 22px; letter-spacing: 1px; line-height: 1.1; text-align: center; }
  .brand-sub { font-size: 11px; letter-spacing: 6px; }
  .card-front .brand { margin-top: 62px; }
  .card-back .brand-mark { background: var(--orange-accent); width: 20px; height: 20px; }
  .card-back .brand-name { font-size: 30px; }
  .card-back .brand-sub { font-size: 14px; letter-spacing: 8px; }
  .card-back .brand { margin-top: -20px; }

  .person-name { position: relative; margin-top: 26px; font-size: 19px; color: var(--ink-dark); letter-spacing: 0.5px; }
  .contact { position: relative; margin-top: 16px; text-align: center; color: var(--white); line-height: 1.35; }
  .contact .phone { font-size: 18px; letter-spacing: 2px; }
  .contact .line { font-size: 13px; letter-spacing: 1px; }

  .tagline {
    position: absolute; bottom: 30px; left: 0; right: 0; text-align: center;
    color: var(--orange-accent); font-size: 10.5px; letter-spacing: 3.2px;
  }
</style>
</head>
<body>
<main class="canvas">
  <section class="card card-front">
    <svg class="card-edges" viewBox="0 0 520 300" aria-hidden="true">
      <polygon points="0,30 12,42 12,258 0,270" fill="var(--ink-dark)"/>
      <polygon points="520,30 508,42 508,258 520,270" fill="var(--ink-dark)"/>
    </svg>
    <div class="brand">
      <span class="brand-mark"></span>
      <span class="brand-name">SUMMIT FLOOR</span>
      <span class="brand-sub">INSPECTIONS</span>
    </div>
    <p class="person-name">DANA MERROW</p>
    <div class="contact">
      <p class="phone">303-555-01420</p>
      <p class="line">dana@summitfloor.example</p>
      <p class="line">summitfloor.example</p>
    </div>
  </section>

  <section class="card card-back">
    <svg class="card-edges" viewBox="0 0 520 300" aria-hidden="true">
      <polygon points="0,30 12,42 12,258 0,270" fill="var(--orange-accent)"/>
      <polygon points="520,30 508,42 508,258 520,270" fill="var(--orange-accent)"/>
    </svg>
    <div class="brand">
      <span class="brand-mark"></span>
      <span class="brand-name">SUMMIT FLOOR</span>
      <span class="brand-sub">INSPECTIONS</span>
    </div>
    <p class="tagline">CERTIFIED FLOOR COVERING INSPECTIONS &amp; CONSULTING</p>
  </section>
</main>
</body>
</html>
```